I am looking for business cards and letterhead

I want a high-level look for CEO's who want a concierge level leadership consultant and organization development strategist

This needs to go with my brand: simple, elegant, clean. Please improve on this design while using these fonts and colors

Here is my website: CorinneValdez.com

```html
<!DOCTYPE html>
<html lang="en">
<head>
<meta charset="utf-8">
<title>Corinne Valdez — Business Cards</title>
<link rel="stylesheet" href="https://fonts.googleapis.com/css2?family=Montserrat:wght@400;500;700&display=swap">
<style>
  :root {
    --page: #e9e7e2;
    --gold: #e3c67f;
    --gold-light: #f0d99c;
    --gold-deep: #c9a95e;
    --ink: #151515;
    --white: #ffffff;
    --blue: #1f5fb5;
    --text-light: #f2f2f2;
  }
  html, body {
    margin: 0;
    width: 1200px;
    height: 900px;
    overflow: hidden;
    background: var(--page);
    font-family: "Montserrat", sans-serif;
  }
  .sheet {
    position: relative;
    width: 1200px;
    height: 900px;
    display: flex;
    align-items: center;
    justify-content: center;
    gap: 40px;
  }
  .card {
    position: relative;
    width: 520px;
    height: 300px;
    border-radius: 24px;
    overflow: hidden;
    box-shadow: 0 10px 30px rgba(0,0,0,0.18);
  }
  .card-art { position: absolute; left: 0; top: 0; }

  /* Front */
  .card-front { background: var(--gold); }
  .front-texture {
    position: absolute; inset: 0;
    background: radial-gradient(circle at 50% 50%, var(--gold-light) 0%, var(--gold) 45%, var(--gold-deep) 100%);
  }
  .front-mark {
    position: absolute;
    left: 50%; top: 50%;
    transform: translate(-50%, -50%);
    width: 120px;
    text-align: center;
    font-weight: 700;
    font-size: 15px;
    line-height: 1.2;
    color: var(--blue);
  }

  /* Back */
  .card-back { background: var(--ink); }
  .back-mark {
    position: absolute;
    left: 140px; top: 150px;
    transform: translate(-50%, -50%);
    width: 150px;
    text-align: center;
    font-weight: 700;
    font-size: 19px;
    line-height: 1.2;
    color: var(--blue);
  }
  .back-details {
    position: absolute;
    left: 306px; top: 40px;
    width: 200px;
    color: var(--text-light);
  }
  .holder-name {
    margin: 0;
    font-size: 20px;
    font-weight: 700;
    line-height: 1.2;
    color: var(--blue);
    white-space: nowrap;
  }
  .holder-title {
    margin: 4px 0 24px;
    font-size: 11px;
    font-weight: 400;
    letter-spacing: 0.3px;
  }
  .holder-address {
    margin: 0 0 24px;
    font-size: 11px;
    line-height: 1.5;
    font-style: normal;
  }
  .contact-list { list-style: none; margin: 0; padding: 0; }
  .contact-list li {
    display: flex; align-items: center; gap: 7px;
    font-size: 11px;
    line-height: 1.3;
    margin-bottom: 7px;
    white-space: nowrap;
  }
  .contact-icon {
    position: static;
    display: block;
    width: 11px; height: 11px;
    flex: none;
  }
</style>
</head>
<body>
<main class="sheet">

  <section class="card card-front" aria-label="Card front">
    <div class="front-texture" role="img" aria-label="Gold finish with fine concentric embossed rings"></div>
    <svg class="card-art" width="520" height="300" viewBox="0 0 520 300" aria-hidden="true">
      <circle cx="260" cy="150" r="80" fill="none" stroke="var(--white)" stroke-width="2"/>
      <circle cx="260" cy="150" r="73" fill="none" stroke="var(--white)" stroke-width="3"/>
      <circle cx="260" cy="150" r="67" fill="none" stroke="var(--white)" stroke-width="1.5"/>
    </svg>
    <div class="front-mark">Corinne Valdez</div>
  </section>

  <section class="card card-back" aria-label="Card back">
    <svg class="card-art" width="520" height="300" viewBox="0 0 520 300" aria-hidden="true">
      <rect x="0" y="0" width="140" height="300" fill="var(--white)"/>
      <circle cx="140" cy="150" r="152" fill="var(--gold)"/>
      <circle cx="136" cy="150" r="148" fill="var(--white)"/>
      <circle cx="140" cy="150" r="118" fill="none" stroke="var(--gold)" stroke-width="4"/>
      <circle cx="140" cy="150" r="110" fill="none" stroke="var(--gold)" stroke-width="2"/>
      <circle cx="140" cy="150" r="104" fill="none" stroke="var(--gold)" stroke-width="3"/>
    </svg>
    <div class="back-mark">Corinne Valdez</div>

    <div class="back-details">
      <h1 class="holder-name">Corinne Valdez</h1>
      <p class="holder-title">Managing Director</p>
      <address class="holder-address">Your address, City<br>State, Zip 1234</address>
      <ul class="contact-list">
        <li>
          <svg class="contact-icon" viewBox="0 0 24 24" aria-hidden="true"><path fill="#1f5fb5" d="M6.6 10.8a15 15 0 0 0 6.6 6.6l2.2-2.2a1 1 0 0 1 1-.25 11.4 11.4 0 0 0 3.6.57 1 1 0 0 1 1 1V20a1 1 0 0 1-1 1A17 17 0 0 1 3 4a1 1 0 0 1 1-1h3.5a1 1 0 0 1 1 1c0 1.25.2 2.45.57 3.57a1 1 0 0 1-.25 1z"/></svg>
          <span>123 456 789</span>
        </li>
        <li>
          <svg class="contact-icon" viewBox="0 0 24 24" aria-hidden="true"><path d="M2 5h20v14H2z M2 5l10 8 10-8" fill="none" stroke="#1f5fb5" stroke-width="2.4"/></svg>
          <span>info@CorinneValdez.com</span>
        </li>
        <li>
          <svg class="contact-icon" viewBox="0 0 24 24" aria-hidden="true"><circle cx="12" cy="12" r="9" fill="none" stroke="#1f5fb5" stroke-width="2.4"/><path d="M3 12h18M12 3c3 3 3 15 0 18M12 3c-3 3-3 15 0 18" fill="none" stroke="#1f5fb5" stroke-width="1.8"/></svg>
          <span>CorinneValdez.com</span>
        </li>
      </ul>
    </div>
  </section>

</main>
</body>
</html>
```